Marlow Crest Homes Needs Business Card Design

Looking for a unique modern business card to fit my new Logo.
Name: Dean Marlow
Company: Marlow Crest Homes, LLC
Tag Line: Forever Framed Right
Email: marlowcresthomes@mailvista.test
Phone: (253) 555-0187
Website: www.marlowcresthomes.test
License: MARLOCH462QT

```html
<!DOCTYPE html>
<html lang="en">
<head>
<meta charset="utf-8">
<title>Marlow Crest Homes — Business Card</title>
<link href="https://fonts.googleapis.com/css2?family=Montserrat:wght@400;500;600;700&display=swap" rel="stylesheet">
<style>
  :root {
    --brand-blue: #3397cc;
    --ink: #141414;
    --muted: #444444;
    --card-white: #ffffff;
    --backdrop: #ece9e4;
  }
  * { margin: 0; padding: 0; box-sizing: border-box; }
  html, body { width: 900px; height: 1200px; overflow: hidden; }
  body {
    background: var(--backdrop);
    font-family: "Montserrat", Arial, sans-serif;
    position: relative;
  }
  .card {
    position: absolute;
    left: 80px;
    width: 742px;
    height: 440px;
    border-radius: 30px;
    overflow: hidden;
    box-shadow: 0 4px 10px rgba(0,0,0,0.25);
  }
  .card--front { top: 132px; background: var(--card-white); }
  .card--back { top: 638px; background: var(--brand-blue); }

  .wordmark {
    position: absolute;
    display: flex;
    align-items: center;
    gap: 22px;
    font-weight: 700;
    letter-spacing: 0.5px;
    white-space: nowrap;
  }
  .wordmark__square { width: 56px; height: 56px; flex: none; }
  .wordmark__name { font-size: 42px; line-height: 1; }
  .card--front .wordmark { left: 105px; top: 128px; }
  .card--front .wordmark__square { background: var(--brand-blue); }
  .card--front .wordmark__name { color: var(--ink); }
  .card--back .wordmark { left: 105px; top: 190px; }
  .card--back .wordmark__square { background: var(--card-white); }
  .card--back .wordmark__name { color: var(--card-white); }

  .person {
    position: absolute;
    right: 424px;
    top: 286px;
    text-align: right;
  }
  .person__name { font-size: 26px; font-weight: 700; color: var(--brand-blue); line-height: 1.1; }
  .person__title { font-size: 16px; font-weight: 400; color: var(--muted); margin-top: 6px; }

  .divider {
    position: absolute;
    left: 354px;
    top: 288px;
    width: 2px;
    height: 62px;
    background: var(--brand-blue);
  }

  .contacts {
    position: absolute;
    left: 390px;
    top: 284px;
    list-style: none;
  }
  .contacts li {
    display: flex;
    align-items: center;
    gap: 10px;
    height: 22px;
    font-size: 16px;
    color: var(--ink);
  }
  .contacts svg { width: 13px; height: 13px; fill: var(--brand-blue); flex: none; }

  .license-band {
    position: absolute;
    left: 0;
    top: 383px;
    width: 100%;
    height: 30px;
    background: var(--brand-blue);
    color: var(--card-white);
    font-size: 16px;
    font-weight: 500;
    text-align: center;
    line-height: 30px;
  }
</style>
</head>
<body>
  <section class="card card--front">
    <div class="wordmark">
      <span class="wordmark__square"></span>
      <span class="wordmark__name">MARLOW CREST HOMES</span>
    </div>

    <div class="person">
      <p class="person__name">Dean Marlow</p>
      <p class="person__title">CEO &amp; Founder</p>
    </div>
    <div class="divider"></div>

    <ul class="contacts">
      <li>
        <svg viewBox="0 0 16 16" aria-hidden="true"><path d="M3 1h3l1.5 4-2 1.3a9 9 0 0 0 4.2 4.2L11 8.5l4 1.5v3a2 2 0 0 1-2 2A12 12 0 0 1 1 3a2 2 0 0 1 2-2z"/></svg>
        <span>(253) 555-0187</span>
      </li>
      <li>
        <svg viewBox="0 0 16 16" aria-hidden="true"><path d="M1 3h14v10H1z M1 3l7 5 7-5" /><path d="M1.5 3.5 8 8.2l6.5-4.7" fill="none" stroke="#fff" stroke-width="1.2"/></svg>
        <span>marlowcresthomes@mailvista.test</span>
      </li>
      <li>
        <svg viewBox="0 0 16 16" aria-hidden="true"><circle cx="8" cy="8" r="7"/><path d="M1 8h14M8 1c-3 3-3 11 0 14M8 1c3 3 3 11 0 14" fill="none" stroke="#fff" stroke-width="1"/></svg>
        <span>www.marlowcresthomes.test</span>
      </li>
    </ul>

    <div class="license-band">License: MARLOCH462QT</div>
  </section>

  <section class="card card--back">
    <div class="wordmark">
      <span class="wordmark__square"></span>
      <span class="wordmark__name">MARLOW CREST HOMES</span>
    </div>
  </section>
</body>
</html>
```